PowerPoint Design Project

We need a powerpoint design for our consulting company, Brindle Consulting. We provide technology strategy and solutioning services, with an emphasis on cloud technology. More information about our services can be found at www.brindleconsulting-example.com

We are looking for a design that is professional, but not corporate stuffy. The design needs to use our primary colors in our brand.
Updates

Reason: We need to iterate on some of the great designs, plus, many people have not had a chance to submit their design yet.

Reason: We had a lot of people accept the project, but not all of them have responded yet. We wanted to get them some time, plus, ask a couple of people to make some minor revisions.

Target Market(s)

Technology buyers between the ages of 30-55 at Vantor 1000 companies

Industry/Entity Type

It Company

Requirements
Must have
• Must follow our logo colors.
Must have at least a cover slide and interior content slide.
Should not have
• Should not contain anything cartoonish or anything with lots of clouds

```html
<!DOCTYPE html>
<html lang="en">
<head>
<meta charset="utf-8">
<title>Brindle Consulting – Presentation Template</title>
<link rel="stylesheet" href="https://fonts.googleapis.com/css2?family=Arimo:wght@400;700&display=swap">
<style>
  :root {
    --canvas-bg: #d6d6d6;
    --brand-deep: #1a6f93;
    --brand-mid: #2289b2;
    --brand-light: #3aa6cc;
    --brand-text: #1f86ad;
    --bar-dark: #2a5670;
    --bar-teal: #2392b3;
    --slide-white: #ffffff;
    --axis-grey: #9a9a9a;
    --label-grey: #444444;
  }
  * { box-sizing: border-box; margin: 0; padding: 0; }
  html, body { width: 1200px; height: 1200px; overflow: hidden; }
  body {
    background: var(--canvas-bg);
    font-family: "Arimo", Arial, sans-serif;
    position: relative;
  }
  .slide {
    position: absolute;
    width: 500px;
    height: 375px;
    background: var(--slide-white);
    overflow: hidden;
    box-shadow: 0 4px 14px rgba(0,0,0,0.25);
  }
  .slide--cover   { left: 60px;  top: 28px; }
  .slide--text    { left: 640px; top: 28px; }
  .slide--bullets { left: 60px;  top: 423px; }
  .slide--chart   { left: 640px; top: 423px; }
  .slide--closing { left: 350px; top: 818px; }

  .brand-field {
    position: absolute; inset: 0;
    background: radial-gradient(ellipse at 45% 40%, var(--brand-light) 0%, var(--brand-mid) 45%, var(--brand-deep) 100%);
  }
  .header-band {
    position: absolute; left: 0; top: 0; right: 0; height: 68px;
    background: radial-gradient(ellipse at 40% 0%, var(--brand-light) 0%, var(--brand-mid) 70%);
  }
  .slide-title {
    position: absolute; left: 66px; top: 18px;
    color: var(--slide-white);
    font-size: 28px; font-weight: 700;
  }
  .footer-rule {
    position: absolute; left: 0; right: 0; bottom: 0; height: 7px;
    background: var(--brand-mid);
  }
  .body-copy {
    position: absolute; left: 36px; right: 30px; top: 92px;
    color: var(--brand-text);
    font-size: 16px; line-height: 1.55;
  }
  .body-copy strong { font-weight: 700; }
  .bullet-list { list-style: none; }
  .bullet-list li { position: relative; padding-left: 20px; margin-bottom: 3px; }
  .bullet-list li::before {
    content: ""; position: absolute; left: 2px; top: 7px;
    width: 8px; height: 8px; border-radius: 50%;
    background: var(--brand-text);
  }

  .company-name {
    position: absolute;
    font-weight: 400;
  }
  .company-name--footer {
    right: 18px; bottom: 16px;
    color: var(--brand-text); font-size: 12px;
  }
  .company-name--cover {
    left: 34px; bottom: 36px;
    color: var(--slide-white); font-size: 22px;
  }
  .chart { position: absolute; left: 16px; top: 80px; }
</style>
</head>
<body>

  <section class="slide slide--cover" aria-label="Cover slide">
    <div class="brand-field" role="img" aria-label="Blue brand field with a pattern of pale translucent circles"></div>
    <p class="company-name company-name--cover">Brindle Consulting</p>
  </section>

  <section class="slide slide--text" aria-label="Text slide">
    <div class="header-band" role="img" aria-label="Blue header band with pale translucent circles"></div>
    <h2 class="slide-title">Title</h2>
    <p class="body-copy">Lorem ipsum dolor sit amet, consectetur adipiscing elit. Nam et dolor scelerisque, condimentum sapien id, posuere justo. <strong>Interdum et malesuada</strong> fames ac ante ipsum primis in faucibus. Pellentesque vel auctor mi. Class aptent taciti sociosqu ad litora torquent per conubia nostra, per inceptos himenaeos.</p>
    <p class="company-name company-name--footer">Brindle Consulting</p>
    <div class="footer-rule"></div>
  </section>

  <section class="slide slide--bullets" aria-label="Bullet slide">
    <div class="header-band" role="img" aria-label="Blue header band with pale translucent circles"></div>
    <h2 class="slide-title">Title</h2>
    <ul class="body-copy bullet-list">
      <li>Lorem ipsum dolor sit amet, consectetur adipiscing elit.</li>
      <li>Nam et dolor scelerisque, condimentum sapien id, posuere justo.</li>
      <li><strong>Interdum et malesuada</strong> fames ac ante ipsum primis in faucibus.</li>
      <li>Pellentesque vel auctor mi.</li>
      <li>Class aptent taciti sociosqu ad litora torquent per conubia nostra, per inceptos himenaeos.</li>
    </ul>
    <div class="footer-rule"></div>
  </section>

  <section class="slide slide--chart" aria-label="Chart slide">
    <div class="header-band" role="img" aria-label="Blue header band with pale translucent circles"></div>
    <h2 class="slide-title">Title</h2>
    <svg class="chart" width="470" height="270" viewBox="0 0 470 270" font-family="Arimo, Arial, sans-serif">
      <g stroke="var(--axis-grey)" stroke-width="1">
        <line x1="60" y1="20" x2="60" y2="230"/>
        <line x1="117" y1="20" x2="117" y2="230" stroke-opacity="0.4"/>
        <line x1="175" y1="20" x2="175" y2="230" stroke-opacity="0.4"/>
        <line x1="232" y1="20" x2="232" y2="230" stroke-opacity="0.4"/>
        <line x1="290" y1="20" x2="290" y2="230" stroke-opacity="0.4"/>
      </g>
      <g font-size="11" fill="var(--label-grey)" text-anchor="end">
        <text x="52" y="52">2007</text>
        <text x="52" y="102">2008</text>
        <text x="52" y="152">2009</text>
        <text x="52" y="202">2010</text>
      </g>
      <g>
        <rect x="60" y="30" width="46"  height="16" fill="var(--bar-dark)"/>
        <rect x="60" y="46" width="150" height="16" fill="var(--bar-teal)"/>
        <rect x="60" y="80" width="80"  height="16" fill="var(--bar-dark)"/>
        <rect x="60" y="96" width="120" height="16" fill="var(--bar-teal)"/>
        <rect x="60" y="130" width="138" height="16" fill="var(--bar-dark)"/>
        <rect x="60" y="146" width="172" height="16" fill="var(--bar-teal)"/>
        <rect x="60" y="180" width="230" height="16" fill="var(--bar-dark)"/>
        <rect x="60" y="196" width="138" height="16" fill="var(--bar-teal)"/>
      </g>
      <g font-size="11" fill="var(--label-grey)" text-anchor="middle">
        <text x="60" y="250">0</text>
        <text x="117" y="250">25</text>
        <text x="175" y="250">50</text>
        <text x="232" y="250">75</text>
        <text x="290" y="250">100</text>
      </g>
      <g font-size="11" fill="var(--label-grey)">
        <rect x="320" y="40" width="10" height="10" fill="var(--bar-dark)"/>
        <text x="336" y="49">Region 1</text>
        <rect x="320" y="62" width="10" height="10" fill="var(--bar-teal)"/>
        <text x="336" y="71">Region 2</text>
      </g>
    </svg>
    <div class="footer-rule"></div>
  </section>

  <section class="slide slide--closing" aria-label="Closing slide">
    <div class="brand-field" role="img" aria-label="Blue brand field with a pattern of pale translucent circles"></div>
    <p class="company-name company-name--cover">Brindle Consulting</p>
  </section>

</body>
</html>
```